We are launching in December, a range of supplements and vitamins.

We have just made an amend to the mission statement and how we are going to give back to society. Please can you add both to the packaging:

Verdant’s purpose is to support health, wellbeing and longevity, so that we can all thrive in the modern world; an environment so alien to that in which we evolved. Embracing technology, research and science, we harness nature’s goodness - enabling us all to love life – naturally.

Twice Kind Promise. For each and every Verdant supplement you take, we provide a supplement to an under nourished child.

For every supplement we sell: £1 goes to the charity ‘Little Lights Fund’ and in addition we provide one healthy meal to an under privileged child in India.

My name is Mark Holloway and I own several companies including www.quartzelle.com (you can check me out on Infopedex – I am not the football referee nor the rocket scientist, but the entrepreneur) . Over the past 2 years I have been writing a book to help people live more healthily and it launches in December. It’s called Verdant Way. While doing my research for the book, I came to realise that most supplements and vitamin products on the market are rubbish! Most are made for profit and not for the benefit of the consumer. I want to change all of that. Howard Pellow is patron of a charity I set up with my brother Paul Holloway and together we have built 11 schools in Asia. I am hoping to get Howards help in getting my supplements to market.

Positioning of our supplements - In a world where so much has changed from the one our bodies were designed to thrive, at Verdant Supplements we are driven by one purpose; to globally provide healthy support to life in the 21st century. While the roots of our wellbeing supplements date back beyond 10,000BC, we embrace modern technology and science, to encapsulate powerful phytonutrients, herbs and other goodness. The essence of which is to promote health, happiness and longevity.

So what are we looking for in the design? Something that stands out. Something that looks professional. A design and concept that can role out across 24 different products. Some products are simple, just one ingredient, such as vitamin D3, Magnesium, Garlic Extracts etc, and others are our own formulas where there are up to 30 different ingredients. You can contact me at any time with questions at Mark@verdantway-example.com

Target Market(s)

Male & Female 20 years plus, mainly UK

Industry/Entity Type

Medical

Logo Text

VERDANT - Sub heading = Thriving Days Gently

Colors

Designer to choose colors to be used in the design.

Requirements
Must have
• see attached powerpoint.
• We have just made an amend to the mission statement and how we are going to give back to society. Please can you add both to the packaging:
• Verdant’s purpose is to support health, wellbeing and longevity, so that we can all thrive in the modern world; an environment so alien to that in which we evolved. Embracing technology, research and science, we harness nature’s goodness - enabling us all to love life – naturally.
• Twice Kind Promise. For each and every Verdant supplement you take, we provide a supplement to an under nourished child.
Nice to have
• see attached powerpoint
Should not have
• see attached powerpoint

```html
<!DOCTYPE html>
<html lang="en">
<head>
<meta charset="utf-8">
<title>Verdant Supplements – Vitamin D3 Back Label</title>
<link rel="stylesheet" href="https://fonts.googleapis.com/css2?family=Exo+2:wght@300;400;600&family=Ubuntu:wght@400;500;700&display=swap">
<style>
  :root {
    --canvas-bg: #e6e7e8;
    --label-light: #e3ebf2;
    --label-mid: #cfdce8;
    --panel-blue: #a9c7dd;
    --panel-blue-light: #bcd4e6;
    --panel-text: #ffffff;
    --tab-dark: #3b3b3d;
    --tab-text: #ffffff;
    --warning-yellow: #f2c400;
    --body-text: #2e3033;
    --accent-blue: #5f8fb3;
    --web-faint: #a7b4bf;
    --web-strong: #3a3d40;
    --badge: #c3cfda;
  }
  * { margin: 0; padding: 0; box-sizing: border-box; }
  html, body {
    width: 1200px;
    height: 1200px;
    overflow: hidden;
    background: var(--canvas-bg);
  }
  .canvas {
    position: relative;
    width: 1200px;
    height: 1200px;
    background: var(--canvas-bg);
  }
  .back-label {
    position: absolute;
    left: 290px;
    top: 420px;
    width: 640px;
    height: 600px;
    background: linear-gradient(180deg, var(--label-light) 0%, var(--label-mid) 100%);
    overflow: hidden;
  }
  .info-panel {
    position: absolute;
    left: 0;
    top: 0;
    width: 380px;
    height: 300px;
    background: linear-gradient(180deg, var(--panel-blue) 0%, var(--panel-blue-light) 100%);
    border-bottom-right-radius: 14px;
    padding: 24px 20px 0 22px;
  }
  .info-panel p {
    font-family: "Exo 2", sans-serif;
    font-weight: 300;
    font-size: 17.5px;
    line-height: 23px;
    color: var(--panel-text);
  }
  .info-tab {
    position: absolute;
    left: 0;
    top: 282px;
    width: 238px;
    height: 46px;
    background: var(--tab-dark);
    border-top-right-radius: 12px;
    border-bottom-right-radius: 12px;
    display: flex;
    align-items: center;
    padding-left: 24px;
    gap: 10px;
  }
  .info-tab svg { width: 20px; height: 18px; flex: none; }
  .info-tab h2 {
    font-family: "Ubuntu", sans-serif;
    font-weight: 700;
    font-size: 16px;
    color: var(--tab-text);
    letter-spacing: 0.2px;
  }
  .warnings {
    position: absolute;
    left: 24px;
    top: 346px;
    width: 340px;
    font-family: "Ubuntu", sans-serif;
    font-weight: 500;
    font-size: 12.6px;
    line-height: 15px;
    color: var(--body-text);
    letter-spacing: 0.1px;
  }
  .web-address {
    position: absolute;
    left: 30px;
    top: 552px;
    font-family: "Ubuntu", sans-serif;
    font-size: 13.5px;
    color: var(--web-faint);
  }
  .web-address strong {
    font-weight: 500;
    color: var(--web-strong);
  }
  .brand-column {
    position: absolute;
    left: 404px;
    top: 24px;
    width: 214px;
    font-family: "Exo 2", sans-serif;
    color: var(--body-text);
  }
  .brand-column h3 {
    font-weight: 600;
    font-size: 13px;
    letter-spacing: 0.6px;
    text-transform: uppercase;
    color: var(--accent-blue);
    margin-bottom: 6px;
  }
  .brand-column p {
    font-weight: 400;
    font-size: 12px;
    line-height: 16px;
    margin-bottom: 18px;
  }
  .origin-badge {
    position: absolute;
    left: 404px;
    top: 520px;
    width: 50px;
    height: 50px;
    border-radius: 50%;
    background: var(--badge);
  }
</style>
</head>
<body>
  <main class="canvas">
    <section class="back-label" aria-label="Vitamin D3 back label">
      <div class="info-panel">
        <p>Each tablet contains vitamin D3 at an exceptional 5000iu. Lack of vitamin D can lead to bone deformities such as rickets in children and bone pain caused by a condition called osteomalacia in adults. The body creates vitamin D from direct sunlight on the skin when outdoors but between october and early march we do not get enough vitamin D from sunlight.</p>
      </div>

      <div class="info-tab">
        <svg viewBox="0 0 20 18" aria-hidden="true">
          <path d="M10 1 L19 17 L1 17 Z" fill="var(--warning-yellow)" stroke="var(--warning-yellow)" stroke-linejoin="round" stroke-width="1.5"/>
          <rect x="9.1" y="6" width="1.8" height="6" fill="var(--tab-dark)"/>
          <rect x="9.1" y="13.3" width="1.8" height="1.8" fill="var(--tab-dark)"/>
        </svg>
        <h2>Important Information</h2>
      </div>

      <p class="warnings">Food supplements should not be used as a substitute for a balanced diet and healthy lifestyle. If you are pregnant, breastfeeding, taking prescription medication or under medical supervision it is advisable to consult a GP prior to taking any supplements. Discontinue use and consult a GP if adverse reactions occur. Do not exceed stated dose. Store in a cool, dry place. Keep away from children at all times. Do not use if seal under cap is broken.</p>

      <p class="web-address">www.<strong>verdantsupplements.</strong>com</p>

      <div class="brand-column">
        <h3>Our Purpose</h3>
        <p>Verdant’s purpose is to support health, wellbeing and longevity, so that we can all thrive in the modern world; an environment so alien to that in which we evolved. Embracing technology, research and science, we harness nature’s goodness - enabling us all to love life – naturally.</p>
        <h3>Twice Kind Promise</h3>
        <p>For each and every Verdant supplement you take, we provide a supplement to an under nourished child.</p>
      </div>

      <div class="origin-badge" role="img" aria-label="Made in UK badge"></div>
    </section>
  </main>
</body>
</html>
```